Proverbs Sermon Series Artwork

We are in need of new artwork for an upcoming sermon series that our Senior Pastor will be preaching for at least the next 6 months. This graphic will be used extensively on our app, website, and in worship services and needs to be of excellent quality and also provide meaning behind the entirety of the series. Proverbs is a very rich book of the Bible that deals with wisdom and how to live according to God's principles. The graphic needs to reflect this truth and communicate to those who see it that there are different ways that each of us can choose to live.
We are very flexible on the goal of this piece and don't really have anything in mind. The graphic that is the most professional but also communicated the goal of the sermon series will be the one selected. Please see the must haves to get an idea of different formats we would like to use this graphic in. It will be a key image in the life of our church over the next 6-12 months.
Thanks for looking into this project. I hope you will submit a graphic design and use your God given talents to help us (and make a little money on the side). ArtBazaarly has served us well in the past and we are excited to use it again.
Updates
As of right now, I have 3 good designs from 2 designers. I would love to see the edits made based on feedback provided. I think there is a lot of potential in all 3 designs. If you have questions please let me know. After all artwork is submitted I will be presenting it to the senior pastor and he will select the one he likes the best. I would like to bring him 5 designs so there is still room for some other good submissions from new designers! Also, I uploaded a road sign image. I would like to see something with an image like that from someone.
Target Market(s)
Church members, app users, website visitors
Industry/Entity Type
Religious
Requirements
Must have
- Artwork must include Proverbs in a bold easy to read font. The graphic must also lend itself to different formats. 1920x1080 wide format graphic, 1024x1024 square icon, 1920x692 banner.
Nice to have
- The sermon series is about us having choices on how to live our lives and the goal that we should take God's way instead of ours. This would lend itself well to road signs or maybe something cool with nature. Maybe even a word art as proverbs is a lot of sayings that speak to wisdom of the Christian walk. I'm pretty flexible.
Should not have
- Not overly feminine like most church artwork. This is geared to the whole body, not women.

```html
<!DOCTYPE html>
<html lang="en">
<head>
<meta charset="UTF-8">
<title>Proverbs Sermon Series</title>
<link rel="stylesheet" href="https://fonts.googleapis.com/css2?family=Stardos+Stencil:wght@700&display=swap">
<style>
  :root {
    --frame: #ffffff;
    --violet-deep: #3a1f7a;
    --violet: #6a3ad0;
    --magenta: #d63fe6;
    --pink-glow: #f27ff5;
    --teal-dark: #173a3a;
    --night: #142b2e;
    --title-fill: #ffffff;
    --title-glow: #2fd6e8;
  }
  * { margin: 0; padding: 0; box-sizing: border-box; }
  html, body {
    width: 1200px;
    height: 676px;
    overflow: hidden;
    background: var(--frame);
  }
  .series-art {
    position: relative;
    width: 1200px;
    height: 676px;
    background: var(--frame);
  }
  .scene-backdrop {
    position: absolute;
    left: 12px;
    top: 12px;
    width: 1176px;
    height: 652px;
    background:
      radial-gradient(ellipse 38% 30% at 46% 42%, var(--pink-glow) 0%, rgba(242,127,245,0) 100%),
      linear-gradient(180deg,
        var(--violet-deep) 0%,
        var(--violet) 14%,
        var(--magenta) 34%,
        var(--violet) 52%,
        var(--night) 62%,
        var(--violet) 74%,
        var(--violet-deep) 86%,
        var(--teal-dark) 100%);
  }
  .series-title {
    position: absolute;
    left: 0;
    top: 140px;
    width: 1200px;
    text-align: center;
    font-family: "Stardos Stencil", "Stencil", serif;
    font-weight: 700;
    font-size: 90px;
    line-height: 84px;
    letter-spacing: 0.05em;
    text-transform: uppercase;
    color: var(--title-fill);
    text-shadow:
      0 0 2px var(--title-glow),
      0 0 4px var(--title-glow),
      0 0 10px var(--title-glow);
  }
  .series-title span { display: block; }
</style>
</head>
<body>
  <main class="series-art">
    <div class="scene-backdrop" role="img" aria-label="Blurred purple and pink mountain lake at dusk with streaked light reflections"></div>
    <h1 class="series-title">
      <span class="series-name">Proverbs</span>
      <span class="series-quote">"God Helps</span>
      <span class="series-quote">Those Who Help</span>
      <span class="series-quote">Themselves."</span>
    </h1>
  </main>
</body>
</html>
```